Postcards for Upscale Landscaping Company
Harbor Fern KT
Postcards for Upscale Landscaping Company  - Home and Garden
Creative Brief
Home and Garden
High end homeowners in the $2m+ range. Owner specializing in fine gardening and hedge/topiary trimming.
Need a design for a 5x7 postcard. Front with stamp will just include the logo and and mission statement, name, contact info etc. as on current business card to be submitted.
Tbrantley Tbrantley
I’m not sure we have the card in that file format. I’ll work on it and get Bach to you. Thanks.
sarvesh sarvesh
Hi, Please upload your logo in Ai or PNG file format.

```html
<!DOCTYPE html>
<html lang="en">
<head>
<meta charset="utf-8">
<title>Harbor Fern KT Postcard</title>
<link rel="stylesheet" href="https://fonts.googleapis.com/css2?family=Montserrat:wght@400;600;700;800&family=Cinzel:wght@600&display=swap">
<style>
  :root {
    --page: #ffffff;
    --green: #3fb93a;
    --ink: #1d1d1d;
    --paper: #ffffff;
    --rule: #3a3a3a;
    --lime: #d9f27a;
    --photo-a: #b9d3e6;
    --photo-b: #cfdde6;
  }
  * { box-sizing: border-box; margin: 0; padding: 0; }
  html, body { width: 1200px; height: 876px; overflow: hidden; background: var(--page); }
  body { position: relative; font-family: "Montserrat", Arial, sans-serif; }

  .postcard {
    position: absolute; top: 242px; width: 544px; height: 394px;
    overflow: hidden; box-shadow: 0 3px 10px rgba(0,0,0,.35);
  }

  /* Back side */
  .postcard--back { left: 34px; background: var(--paper); }
  .back__address { position: absolute; left: 0; top: 0; width: 280px; height: 100%; }
  .stamp-box { position: absolute; left: 31px; top: 70px; width: 86px; height: 84px; border: 2px solid var(--rule); }
  .address-line { position: absolute; left: 31px; width: 213px; height: 2px; background: var(--rule); }
  .back__brand {
    position: absolute; left: 280px; top: 0; right: 0; bottom: 0; background: var(--green);
    border-left: 10px solid var(--paper);
    display: flex; flex-direction: column; align-items: center; justify-content: center;
  }
  .back__brand::before {
    content: ""; position: absolute; left: 4px; top: 0; bottom: 0; width: 2px; background: var(--paper);
  }
  .brand-mark { width: 46px; height: 46px; border-radius: 50%; background: var(--ink); margin-bottom: 14px; }
  .brand-name { font-family: "Cinzel", Georgia, serif; font-weight: 600; font-size: 21px; color: var(--ink); letter-spacing: .5px; }
  .brand-sub { font-family: "Cinzel", Georgia, serif; font-weight: 600; font-size: 8px; color: var(--ink); letter-spacing: 2px; margin-top: 2px; }

  /* Front side */
  .postcard--front { left: 624px; background: var(--green); }
  .photo-frame {
    position: absolute; left: 250px; top: -14px; width: 340px; height: 370px;
    border: 8px solid var(--paper); transform: rotate(8deg);
    background: linear-gradient(160deg, var(--photo-a) 0%, var(--photo-b) 100%);
  }
  .front__logo { position: absolute; left: 10px; top: 12px; font-family: "Cinzel", Georgia, serif; font-weight: 600; font-size: 8px; color: var(--ink); line-height: 1.1; }
  .anniversary { position: absolute; left: 58px; top: 22px; width: 160px; text-align: center; color: var(--ink); }
  .anniversary__num { font-family: "Cinzel", Georgia, serif; font-size: 46px; font-weight: 600; line-height: 1; }
  .anniversary__word { font-size: 12px; font-weight: 800; letter-spacing: 2px; }
  .ribbon {
    display: inline-block; margin-top: 8px; background: var(--ink); color: #fff;
    font-size: 10px; font-weight: 600; padding: 5px 18px; transform: rotate(-4deg);
  }
  .headline { position: absolute; left: 10px; top: 196px; color: #fff; font-weight: 700; font-size: 27px; }
  .tagline { position: absolute; left: 10px; top: 230px; width: 200px; color: #fff; font-size: 9px; line-height: 1.2; }
  .owner-name { position: absolute; left: 10px; top: 262px; color: var(--lime); font-weight: 700; font-size: 13px; }
  .owner-role { position: absolute; left: 10px; top: 282px; background: var(--ink); color: #fff; font-size: 10px; font-weight: 600; padding: 5px 8px 5px 6px; }
  .phone { position: absolute; left: 10px; top: 317px; color: #fff; font-weight: 700; font-size: 20px; }
  .contact-bar {
    position: absolute; left: 0; right: 0; bottom: 10px; height: 28px; background: var(--paper);
    display: flex; align-items: center; gap: 50px; padding-left: 12px;
    font-size: 8px; color: var(--ink);
  }
</style>
</head>
<body>
  <section class="postcard postcard--back">
    <div class="back__address">
      <div class="stamp-box"></div>
      <div class="address-line" style="top:195px"></div>
      <div class="address-line" style="top:231px"></div>
      <div class="address-line" style="top:267px"></div>
      <div class="address-line" style="top:315px"></div>
    </div>
    <div class="back__brand">
      <div class="brand-mark"></div>
      <div class="brand-name">HARBOR FERN KT</div>
      <div class="brand-sub">LANDSCAPES</div>
    </div>
  </section>

  <section class="postcard postcard--front">
    <div class="photo-frame" role="img" aria-label="Photo of a white coastal lighthouse"></div>
    <div class="front__logo">HARBOR FERN KT<br>LANDSCAPES</div>
    <div class="anniversary">
      <div class="anniversary__num">15</div>
      <div class="anniversary__word">YEARS</div>
      <div class="ribbon">Experience, specialty</div>
    </div>
    <h1 class="headline">Full Service...</h1>
    <p class="tagline">Specializing in fine gardening and hedge/topiary trimming</p>
    <p class="owner-name">Tom Brantley</p>
    <p class="owner-role">OWNER</p>
    <p class="phone">(555)014-2276</p>
    <div class="contact-bar">
      <span>harborfernkt.com</span>
      <span>tom@harborfernkt.com</span>
    </div>
  </section>
</body>
</html>
```